Premium Cannabis Dispensary - buisness card

The logo is goldish yellow, the writing will be white.
Looking to make a soft touch laminate for the buisness card, or something that feels premium as we are selling premium products.
Buisness name: Tovin Glade
second line: Premium Cannabis & Fine Edibles
phone number: (to be included after)
email: tovinglade@velmora-mail.net
website: https://tovinglade-shop.net (QR code to be created also)
description of buisness:
Tovin Glade is a Dispensary offering delivery across GTA. We strive to help people feel good and provide quality products for the lowest prices.
How To Order:
Visit our website
Text or Email us your order
Payment:
Cash On Delivery
Email Transfer Arrangement is Possible
Target Market(s)
Middle to upper class clientele
Contact Information for Business Card
Number, email, web link, QR code to link, company description
Colors
Designer to choose colors to be used in the design.

```html
<!DOCTYPE html>
<html lang="en">
<head>
<meta charset="utf-8">
<title>Tovin Glade — Business Card</title>
<link rel="stylesheet" href="https://fonts.googleapis.com/css2?family=Cinzel:wght@400;600&family=Roboto+Condensed:wght@400;700&family=Roboto:wght@400;700&display=swap">
<style>
  :root {
    --backdrop: #e4e4e4;
    --card: #0b1d18;
    --card-edge: #112a23;
    --gold: #f2c417;
    --yellow: #ffe20a;
    --white: #ffffff;
    --soft-white: #e8ece9;
  }
  * { box-sizing: border-box; margin: 0; padding: 0; }
  html, body {
    width: 1200px; height: 800px; overflow: hidden;
    background: var(--backdrop);
  }
  .canvas {
    width: 1200px; height: 800px;
    display: flex; align-items: center; justify-content: center; gap: 48px;
  }
  .card {
    width: 520px; height: 300px;
    background: var(--card);
    border-radius: 22px;
    box-shadow: 0 10px 24px rgba(0,0,0,.22);
    position: relative;
    color: var(--white);
  }

  /* Front */
  .card-front { display: flex; align-items: center; }
  .brand {
    width: 270px; padding-left: 44px;
    display: flex; flex-direction: column; align-items: flex-start;
  }
  .brand-mark {
    width: 34px; height: 34px; border-radius: 50%;
    background: var(--gold); margin-bottom: 12px;
  }
  .brand-name {
    font-family: "Cinzel", serif; font-weight: 600;
    font-size: 30px; letter-spacing: 1px; line-height: 1;
    color: var(--white);
  }
  .brand-tagline {
    font-family: "Roboto", sans-serif; font-weight: 700;
    font-size: 11.5px; margin-top: 6px; color: var(--white);
  }
  .contact { padding-left: 10px; }
  .person-name {
    font-family: "Cinzel", serif; font-weight: 400;
    font-size: 22px; letter-spacing: 1.5px; color: var(--white);
  }
  .person-role {
    font-family: "Roboto", sans-serif; font-size: 13px;
    color: var(--gold); margin-top: 2px;
  }
  .rule {
    width: 28px; height: 1px; background: var(--soft-white);
    margin: 12px 0 12px;
  }
  .contact-list { list-style: none; }
  .contact-list li {
    display: flex; align-items: center; gap: 9px;
    font-family: "Roboto", sans-serif; font-size: 12px;
    color: var(--soft-white); line-height: 22px;
  }
  .contact-list svg { width: 13px; height: 13px; flex: none; }

  /* Back */
  .card-back {
    display: flex; flex-direction: column; align-items: center; justify-content: center;
    text-align: center;
    font-family: "Roboto Condensed", sans-serif;
  }
  .back-mark {
    font-family: "Cinzel", serif; font-weight: 600;
    font-size: 30px; letter-spacing: 1px; color: var(--gold);
    margin-bottom: 20px;
  }
  .info-head {
    color: var(--yellow); font-size: 17px; font-weight: 400;
    text-transform: uppercase; letter-spacing: .3px;
  }
  .info-body { color: var(--white); font-size: 16px; margin-top: 2px; }
  .back-rule { width: 26px; height: 1px; background: var(--white); margin: 10px auto; }
  .web { color: var(--yellow); font-size: 15px; margin-top: 4px; }
  .web strong { font-weight: 700; }
</style>
</head>
<body>
<main class="canvas">
  <section class="card card-front">
    <div class="brand">
      <span class="brand-mark"></span>
      <span class="brand-name">Tovin Glade</span>
      <span class="brand-tagline">Premium Cannabis &amp; Fine Edibles</span>
    </div>
    <div class="contact">
      <h1 class="person-name">DARA QUELL</h1>
      <p class="person-role">President</p>
      <div class="rule"></div>
      <ul class="contact-list">
        <li>
          <svg viewBox="0 0 16 16"><path fill="#f2c417" d="M3.6 1.5l2.3 2.6-1.3 1.8c.9 2 2.4 3.5 4.4 4.4l1.8-1.3 2.6 2.3-1.4 2.4C6.6 13.3 2.7 9.4 1.3 3z"/></svg>
          555-014-2297
        </li>
        <li>
          <svg viewBox="0 0 16 16"><rect x="1" y="3" width="14" height="10" rx="1" fill="#f2c417"/><path d="M1.5 3.8L8 9l6.5-5.2" fill="none" stroke="#0b1d18" stroke-width="1.3"/></svg>
          tovinglade@velmora-mail.net
        </li>
        <li>
          <svg viewBox="0 0 16 16"><circle cx="8" cy="8" r="7" fill="#f2c417"/><path d="M1.5 8h13M8 1c2.2 2.2 2.2 11.8 0 14M8 1c-2.2 2.2-2.2 11.8 0 14" fill="none" stroke="#0b1d18" stroke-width="1"/></svg>
          tovinglade-shop.net
        </li>
      </ul>
    </div>
  </section>

  <section class="card card-back">
    <div class="back-mark">Tovin Glade</div>
    <p class="info-head">How to order: Visit our website</p>
    <p class="info-body">Text or Email us your order</p>
    <div class="back-rule"></div>
    <p class="info-head">Payment: Cash on delivery</p>
    <p class="info-body">Email Transfer Arrangement is Possible</p>
    <div class="back-rule"></div>
    <p class="web">www.<strong>tovinglade-shop</strong>.net</p>
  </section>
</main>
</body>
</html>
```